Case Study - template Visual Design

We need to convert our current case study document into something more cosmetically pleasing and easy to read. (primary goal). We also want to make sure the design is reusable for future case studies as well.
Current case study content is uploaded for reference.
Company is Plonex.ai
Target Market(s)
Mid to large Enterprise
Industry/Entity Type
Iot
Font styles to use
Sans Serif
Colors
Designer to choose colors to be used in the design.

```html
<!DOCTYPE html>
<html lang="en">
<head>
<meta charset="utf-8">
<title>Plonex.ai – Machine Learning Case Study</title>
<link href="https://fonts.googleapis.com/css2?family=Oswald:wght@400;500&family=PT+Sans+Narrow:wght@400;700&family=Russo+One&display=swap" rel="stylesheet">
<style>
:root{
  --bg:#ffffff;
  --cover:#5b46a1;
  --cover-art:#6a56ad;
  --bar:#4b4ba6;
  --ink:#3a3a46;
  --accent:#4b4ba6;
  --rule:#b9b5e2;
  --paper:#ffffff;
  --photo:#9a9a9a;
}
*{margin:0;padding:0;box-sizing:border-box}
html,body{width:1200px;height:4444px;overflow:hidden;background:var(--bg)}
body{position:relative;font-family:"PT Sans Narrow",sans-serif;color:var(--ink)}
.page{position:absolute;left:240px;width:696px;height:694px;background:var(--paper);box-shadow:0 6px 22px rgba(0,0,0,.22);overflow:hidden}
.brand{display:flex;align-items:center;gap:6px;font-family:"PT Sans Narrow",sans-serif;font-weight:700;color:var(--ink)}
.brand-square{background:var(--accent)}
/* cover */
.cover-brand{position:absolute;right:74px;top:72px;font-size:38px}
.cover-brand .brand-square{width:30px;height:30px}
.cover-band{position:absolute;left:0;right:0;top:139px;bottom:0;background:var(--cover)}
.cover-art{position:absolute;left:58px;top:40px;width:320px;height:460px;border-radius:18px;background:linear-gradient(160deg,var(--cover-art),var(--cover))}
.cover-title{position:absolute;right:72px;top:358px;text-align:right;color:#fff;font-family:"Oswald",sans-serif}
.cover-title h1{font-weight:500;font-size:42px;line-height:1.1;letter-spacing:.5px}
.cover-title p{font-size:13px;line-height:18px;margin-top:12px;text-transform:uppercase}
/* interior */
.head-bar{position:absolute;left:0;right:0;top:48px;height:22px;background:var(--bar)}
.head-logo{position:absolute;left:104px;top:48px;width:84px;height:22px;background:#fff;padding-left:4px;font-size:17px}
.head-logo .brand-square{width:14px;height:14px}
.head-title{position:absolute;right:52px;top:48px;line-height:22px;color:#fff;font-family:"Oswald",sans-serif;font-size:13px}
.spine{position:absolute;left:104px;top:48px;bottom:0;width:1px;background:var(--rule)}
.head-rule{position:absolute;left:0;right:0;top:138px;height:1px;background:var(--rule)}
.chapter-num{position:absolute;left:50px;top:84px;font-family:"Russo One",sans-serif;font-size:52px;line-height:52px;color:var(--bar)}
.chapter-title{position:absolute;left:112px;top:100px;font-family:"Oswald",sans-serif;font-size:15px;line-height:17px;color:var(--ink);text-transform:uppercase}
.content{position:absolute;left:191px;top:190px;width:453px;font-size:10px;line-height:16.5px;text-align:justify}
.content p{margin-bottom:14px}
.content ul{margin:0 0 14px 20px}
.pull{position:relative;margin:0 0 16px 34px;padding:0 14px 0 15px;color:var(--accent);font-weight:700;text-align:left}
.pull::before{content:"";position:absolute;left:0;top:2px;bottom:-2px;width:5px;border:1px solid var(--accent);border-right:none}
.pull::after{content:"";position:absolute;right:0;top:18px;bottom:-4px;width:5px;border:1px solid var(--accent);border-left:none}
.footnotes{border-top:1px solid var(--ink);width:110px;padding-top:3px;font-size:6px;line-height:8px;white-space:nowrap}
.page-num{position:absolute;right:52px;top:644px;width:52px;border-top:1px solid var(--rule);text-align:right;font-family:"Russo One",sans-serif;font-size:14px;color:var(--ink);padding-top:2px}
/* team */
.member{position:relative;margin-bottom:14px}
.member-photo{position:absolute;left:-74px;top:0;width:62px;height:64px;background:linear-gradient(180deg,#bdbdbd,var(--photo))}
.member strong{display:block}
.contact{list-style:none;font-weight:700}
.contact li{display:flex;align-items:center;gap:20px;height:17px}
.contact svg{width:11px;height:11px;fill:var(--accent)}
</style>
</head>
<body>

<!-- Cover -->
<section class="page" style="top:188px">
  <div class="brand cover-brand"><span class="brand-square"></span>Plonex</div>
  <div class="cover-band">
    <div class="cover-art" role="img" aria-label="Industry icon tiles: gears, heart rate, monitor, ship, oil pump, truck, lab flask, train, factory, mining cart"></div>
  </div>
  <div class="cover-title">
    <h1>MACHINE LEARNING</h1>
    <p>How Plonex drives adoption<br>of predictive maintenance with machine learning</p>
  </div>
</section>

<!-- Page 4 -->
<section class="page" style="top:1026px">
  <div class="head-bar"></div><div class="spine"></div>
  <div class="brand head-logo"><span class="brand-square"></span>Plonex</div>
  <div class="head-title">MACHINE LEARNING</div>
  <div class="chapter-num">2</div>
  <h2 class="chapter-title">How predictive maintenance<br>is ready to deliver bottom-line results</h2>
  <div class="head-rule"></div>
  <div class="content">
    <p>Whenever a business makes an investment in equipment it must also make a commitment to maintain that equipment. Asset failures can often be prevented by committing to a regular, pre-determined schedule of maintenance. This is the preventive maintenance that has been state-of-the-art for many years.</p>
    <p class="pull">With an ability to reduce breakdowns by an average of 70% and lower maintenance costs by an average of 25%, predictive maintenance is no longer an advanced R&amp;D initiative considered only by early adopters.</p>
    <p style="margin-bottom:0">But in many cases, the unique circumstances of how an asset is used will lead to faults happening unpredictably. In fact, only 18% of business assets have an age related failure pattern, and 82% of asset failures appear random, according to Norvale Research<sup>1</sup>. These faults can be enormously disruptive, as they can lead to unexpected downtime, broken timelines, idle employees, unhappy customers, and other competitive disadvantages.</p>
    <p>For many organizations, especially those with high value assets, the maintenance strategies to prevent these disruptions introduce their own inefficiencies. According to Norvale Research<sup>2</sup>:</p>
    <ul>
      <li>40% of scheduled maintenance costs are spent with negligible effect on uptime failure.</li>
      <li>30% of maintenance activities occur too infrequently.</li>
      <li>45% of all maintenance efforts are ineffective.</li>
    </ul>
    <p>In the case of predictive maintenance, advance analytics and data monitoring can more accurately discover patterns before failure occurs. This reliance on data about the actual use of an asset is why predictive maintenance is widely viewed as the lowest-cost approach to maintaining equipment operations.</p>
    <div class="footnotes">1 Source: Norvale Research, Want to get more out of your asset management efforts? Time to include predictive maintenance.<br>https://www.example.com/downloads/cas/asset-report<br>2 Ibid</div>
  </div>
  <div class="page-num">4</div>
</section>

<!-- Page 5 -->
<section class="page" style="top:1866px">
  <div class="head-bar"></div><div class="spine"></div>
  <div class="brand head-logo"><span class="brand-square"></span>Plonex</div>
  <div class="head-title">MACHINE LEARNING</div>
  <div class="chapter-num">2</div>
  <div class="head-rule"></div>
  <div class="content" style="top:194px">
    <p>Today, thanks to a continuous improvement in monitoring and sensing technologies, the practice is becoming more accessible than ever.</p>
    <p>Sensors made possible by the Internet of things (IoT), cloud, and machine learning technologies can now gather real-time data about asset temperature, vibration, location, energy usage, weather impacts, and countless other variables.</p>
    <p>The cost reductions made possible by these technologies have pushed software providers that provide asset and equipment monitoring systems, like computerized machinery maintenance systems (CMMS) and/or Supervisory control and data acquisition (SCADA), for manufacturers to add predictive maintenance capabilities into their feature set.</p>
    <p>Manufacturers of high-end equipment are also providing their own monitoring systems that help them and their clients keep track of the condition of their equipment. These new data streams are being used to predictive breakdowns in advance to initiate maintenance before it occur, and also delay expensive maintenance that is unnecessary due to an asset's actual usage patterns.</p>
    <p class="pull">With an ability to reduce breakdowns by an average of 70% and lower maintenance costs by an average of 25%, predictive maintenance is no longer an advanced R&amp;D initiative considered only by early adopters.</p>
    <p>These advances are now being used by businesses to detect defective products, recommend production optimization, monitor operations in real-time, predict the remaining usefulness of an asset, and identify the root causes of equipment failures that would otherwise lead to millions of dollars in losses.</p>
  </div>
  <div class="page-num">5</div>
</section>

<!-- Page 7 -->
<section class="page" style="top:2716px">
  <div class="head-bar"></div><div class="spine"></div>
  <div class="brand head-logo"><span class="brand-square"></span>Plonex</div>
  <div class="head-title">MACHINE LEARNING</div>
  <div class="chapter-num">3</div>
  <h2 class="chapter-title">Using predictive maintenance<br>in any business environment</h2>
  <div class="head-rule"></div>
  <div class="content">
    <p>At Plonex we are offering businesses of all sizes a way to overcome these challenges. Our approach allows businesses to use the data they already have to quickly assess if predictive maintenance can be applied to their operations. If machine learning predictions can be made with the data we can deploy a solution for immediate use that can scale quickly, and drive bottom-line improvements.</p>
    <p>In many cases, department leaders that bring these new machine learning solutions to their teams have earned recognition among their peers for improving operations. They are also being recognized by executive leadership for bringing new capabilities to the firm that are worth additional investment, simply because the ROI case can be easy to make once a few examples are in hand.</p>
    <p>In one recent example, Plonex worked with the maintenance division of a global manufacturer that provides customers with multimillion-dollar pieces of equipment critical to daily business operations. The division was seeking an efficient way to prototype and validate their vision of adding predictive maintenance into their solution without heavy investments in time and resources.</p>
    <p class="pull">Plonex's fast and low investment approach enabled the division leader to cut through the internal red tape quickly, and they were subsequently recognized for introducing a successful new initiative that grew to be strategic priority project for the entire company.</p>
    <p>They had an excellent team of software engineers that already built a solution that could monitor data coming from their equipment. But they didn't have the capability to apply machine learning models that could use the data to accurately predict failures. The division's team leader sought out Plonex to discover an accessible way to get started.</p>
  </div>
  <div class="page-num">7</div>
</section>

<!-- Page 10 -->
<section class="page" style="top:3568px">
  <div class="head-bar"></div><div class="spine"></div>
  <div class="brand head-logo"><span class="brand-square"></span>Plonex</div>
  <div class="head-title">MACHINE LEARNING</div>
  <div class="chapter-num">5</div>
  <h2 class="chapter-title">Our team<br>contact Plonex</h2>
  <div class="head-rule"></div>
  <div class="content" style="top:192px">
    <p>We are a team of developers and data scientists from leading machine learning companies like Quintrel, Bravara and Sollune, working behind the scenes to deliver exceptional models and experiences.</p>
    <div class="member">
      <div class="member-photo" role="img" aria-label="Portrait photo of Daniel Marsh"></div>
      <strong>Daniel Marsh, CEO.</strong>
      Daniel brings more than 15 years of product management experience building new products and ideas into reality. Prior, Daniel was a data science program manager at Quintrel and global product manager at Halvik Electronics as a member of its smartphone business incubation team. Daniel holds an MBA from the Northfield School of Management and a BS in Electrical Engineering from Caldera University.
    </div>
    <div class="member">
      <div class="member-photo" role="img" aria-label="Portrait photo of Owen Pratt"></div>
      <strong>Owen Pratt, CTO.</strong>
      Owen has been in the software development industry for over 20 years. After undergrad at Ashby College, a number of years at Loanridge.com, and graduating the Linden Hill School of Business, he co-founded Lift Media, Inc. Lift has raised over $20 million in funding and is currently based in San Francisco.
    </div>
    <div class="member">
      <div class="member-photo" role="img" aria-label="Portrait photo of Martin Hale"></div>
      <strong>Martin Hale, CRO.</strong>
      Martin brings 10+ years experience of Sales, Business Development, and Partnerships which during that time he focused on building, launching and scaling products and services. Previously, Martin ran Business Development and Partnerships for Quintrel Cloud, is a former founder of a video streaming company, and IOT enterprise sales at Telvora. Martin holds an MBA from Southgate Institute of Technology, and a BA in Entrepreneurship and Economics from Brookmere State University.
    </div>
    <ul class="contact">
      <li><svg viewBox="0 0 12 12"><circle cx="6" cy="6" r="6"/></svg>https://plonex.ai/</li>
      <li><svg viewBox="0 0 12 12"><path d="M0 2h12v8H0z"/></svg>hello@plonex.ai</li>
      <li><svg viewBox="0 0 12 12"><path d="M3 0l2 3-1.5 1.5a7 7 0 0 0 4 4L9 7l3 2-1.5 2.5C5 12 0 7 .5 1.5z"/></svg>+1 (555) 014-2270</li>
    </ul>
  </div>
  <div class="page-num">10</div>
</section>

</body>
</html>
```